Business Carss for Harborview Church

Need a progressive looking/modern business card design for my church

Target Market(s)

Families and young adults

Industry/Entity Type

Religious

Contact Information for Business Card

2846 Willow Creek Rd.
Frankfort Ky
502-555-0147

Rev. Curtis Holloway
Slogan: Honor God and Make Discies

Font styles to use
Serif
Sans Serif
Decorative
Script

Colors
0555a3
3176b5

Requirements
Should not have
• Should not have a template look
• A unique out of the box look

```html
<!DOCTYPE html>
<html lang="en">
<head>
<meta charset="utf-8">
<title>Harborview Church – Business Card</title>
<link rel="stylesheet" href="https://fonts.googleapis.com/css2?family=Open+Sans:wght@400;600;700&display=swap">
<style>
  :root {
    --brand-blue: #0555a3;
    --brand-blue-light: #3176b5;
    --blue-shade: rgba(4, 70, 136, 0.55);
    --card-dark: #151515;
    --dark-shade: rgba(34, 34, 34, 0.7);
    --page-bg: #2a2a2a;
    --text-light: #f2f2f2;
    --text-silver: #e4e6ea;
    --rule: #2c2c2c;
  }
  * { margin: 0; padding: 0; box-sizing: border-box; }
  html, body {
    width: 1200px;
    height: 900px;
    overflow: hidden;
    background: var(--page-bg);
    font-family: "Open Sans", Arial, sans-serif;
  }
  .canvas {
    position: relative;
    width: 1200px;
    height: 900px;
  }
  .card {
    position: absolute;
    left: 250px;
    width: 700px;
    height: 400px;
    border-radius: 28px;
    overflow: hidden;
  }
  .card--front { top: 30px; background: var(--brand-blue); }
  .card--back { top: 470px; background: var(--card-dark); }

  .background-artwork {
    position: absolute;
    left: 220px;
    top: 0;
    width: 360px;
    height: 400px;
    background: radial-gradient(ellipse at 50% 70%, var(--blue-shade) 0%, rgba(4, 70, 136, 0) 70%);
  }
  .card--back .background-artwork {
    left: 0;
    width: 340px;
    background: radial-gradient(ellipse at 45% 55%, var(--dark-shade) 0%, rgba(34, 34, 34, 0) 70%);
  }

  .front-lockup {
    position: absolute;
    left: 0;
    right: 0;
    top: 160px;
    text-align: center;
  }
  .church-name {
    font-weight: 700;
    letter-spacing: -0.3px;
  }
  .front-lockup .church-name {
    font-size: 48px;
    line-height: 1.1;
    color: var(--text-silver);
  }
  .slogan {
    margin-top: 8px;
    font-size: 15px;
    letter-spacing: 2px;
    color: var(--text-light);
    text-transform: uppercase;
  }

  .back-lockup {
    position: absolute;
    right: 50px;
    top: 85px;
  }
  .back-lockup .church-name {
    font-size: 46px;
    line-height: 1.1;
    color: var(--brand-blue-light);
  }
  .divider {
    position: absolute;
    height: 1px;
    background: var(--rule);
  }
  .divider--top { left: 50px; right: 50px; top: 175px; }
  .divider--name { left: 50px; width: 300px; top: 295px; }

  .address {
    position: absolute;
    right: 50px;
    top: 195px;
    text-align: right;
  }
  .address-label {
    font-size: 16px;
    color: var(--brand-blue-light);
    text-transform: uppercase;
  }
  .address-line {
    font-size: 18px;
    color: var(--text-light);
  }

  .person-name {
    position: absolute;
    left: 50px;
    top: 252px;
    font-size: 23px;
    color: var(--brand-blue-light);
    text-transform: uppercase;
  }
  .phone {
    position: absolute;
    left: 50px;
    top: 322px;
    font-size: 20px;
    color: var(--text-light);
  }
  .phone-label {
    color: var(--brand-blue-light);
    font-weight: 600;
  }
</style>
</head>
<body>
  <main class="canvas">
    <section class="card card--front">
      <div class="background-artwork" role="img" aria-label="Faint church building illustration in darker blue"></div>
      <div class="front-lockup">
        <h1 class="church-name">Harborview Church</h1>
        <p class="slogan">Honor God and Make Discies</p>
      </div>
    </section>

    <section class="card card--back">
      <div class="background-artwork" role="img" aria-label="Faint church building illustration in dark grey"></div>
      <div class="back-lockup">
        <p class="church-name">Harborview Church</p>
      </div>
      <div class="divider divider--top"></div>
      <div class="address">
        <p class="address-label">Harborview Church</p>
        <p class="address-line">2846 Willow Creek Rd. Frankfort Ky</p>
      </div>
      <p class="person-name">Rev. Curtis Holloway</p>
      <div class="divider divider--name"></div>
      <p class="phone"><span class="phone-label">P:</span> 502-555-0147</p>
    </section>
  </main>
</body>
</html>
```